Clear sticker design for packaging

I need 4” diameter clear stickers designed for birthdays, thank you , teachers day and all the other special days to complete my gift packaging. They will go on the top of each tube to differentiate each gift for each occasion. Our design is on craft paper and I’ve uploaded a few examples of what we are trying to achieve. Last picture is the top of our tube where the stickers will be placed. We don’t want too much color unless for Christmas and Valentine’s Day maybe! We are working with black and gold or a mixture of both mostly

```html
<!DOCTYPE html>
<html lang="en">
<head>
<meta charset="utf-8">
<title>Thank You Sticker</title>
<link rel="stylesheet" href="https://fonts.googleapis.com/css2?family=Cabin+Sketch:wght@700&display=swap">
<style>
  :root {
    --paper: #ffffff;
    --ink: #2f2f2f;
    --rim: #1e1e1e;
    --leaf-dark: #dcdcdc;
    --leaf-dark-edge: #cdcdcd;
    --leaf-faint: #f2f2f2;
    --leaf-faint-edge: #eaeaea;
  }
  html, body {
    margin: 0;
    padding: 0;
    width: 1200px;
    height: 2444px;
    overflow: hidden;
    background: var(--paper);
  }
  .canvas {
    position: relative;
    width: 1200px;
    height: 2444px;
  }
  .sticker-art {
    position: absolute;
    left: 0;
    top: 0;
    width: 1200px;
    height: 2444px;
  }
  .greeting {
    position: absolute;
    left: 0;
    width: 1200px;
    margin: 0;
    text-align: center;
    font-family: "Cabin Sketch", "Trebuchet MS", sans-serif;
    font-weight: 700;
    font-size: 196px;
    color: var(--ink);
    line-height: 1;
    letter-spacing: 14px;
    white-space: nowrap;
  }
  .greeting-thank { top: 957px; }
  .greeting-you { top: 1112px; }
</style>
</head>
<body>
<main class="canvas">
  <svg class="sticker-art" width="1200" height="2444" viewBox="0 0 1200 2444">
    <defs>
      <clipPath id="sticker-clip">
        <circle cx="600" cy="1222" r="456"/>
      </clipPath>
      <linearGradient id="leaf-dark-fill" x1="0" y1="0" x2="1" y2="1">
        <stop offset="0" stop-color="var(--leaf-dark)"/>
        <stop offset="1" stop-color="var(--leaf-dark-edge)"/>
      </linearGradient>
      <linearGradient id="leaf-faint-fill" x1="0" y1="0" x2="1" y2="1">
        <stop offset="0" stop-color="var(--leaf-faint)"/>
        <stop offset="1" stop-color="var(--leaf-faint-edge)"/>
      </linearGradient>
    </defs>

    <circle class="sticker-face" cx="600" cy="1222" r="458" fill="var(--paper)"/>

    <g class="leaf-sprigs" clip-path="url(#sticker-clip)">
      <ellipse role="img" aria-label="Dark outlined leaf sprig at top" cx="505" cy="885" rx="90" ry="85" fill="url(#leaf-dark-fill)"/>
      <ellipse role="img" aria-label="Faint grey leaf sprig at upper right" cx="850" cy="935" rx="80" ry="42" fill="url(#leaf-faint-fill)"/>
      <ellipse role="img" aria-label="Faint grey leaf sprig at lower left" cx="405" cy="1505" rx="85" ry="80" fill="url(#leaf-faint-fill)"/>
      <ellipse role="img" aria-label="Dark outlined leaf sprig at lower right" cx="790" cy="1500" rx="110" ry="120" fill="url(#leaf-dark-fill)"/>
    </g>

    <g class="accent-dots" fill="var(--ink)">
      <circle cx="692" cy="929" r="5"/>
      <circle cx="754" cy="923" r="5"/>
      <circle cx="724" cy="963" r="5"/>
      <circle cx="964" cy="1225" r="5"/>
      <circle cx="1019" cy="1219" r="5"/>
      <circle cx="974" cy="1273" r="5"/>
      <circle cx="234" cy="1345" r="5"/>
      <circle cx="291" cy="1363" r="5"/>
      <circle cx="246" cy="1390" r="5"/>
      <circle cx="570" cy="1525" r="5"/>
      <circle cx="534" cy="1555" r="5"/>
      <circle cx="576" cy="1581" r="5"/>
    </g>

    <circle class="sticker-rim" cx="600" cy="1222" r="458" fill="none" stroke="var(--rim)" stroke-width="2"/>
  </svg>

  <h1 class="greeting greeting-thank">THANK</h1>
  <p class="greeting greeting-you">YOU</p>
</main>
</body>
</html>
```